Gutschein-Design für Verkauf von hochwertigem Bisonfleisch
Zielgruppe
Das Unternehmen verkauft sehr hochwertiges, kanadisches Bisonfleisch über den Online-Shop (weidenkorn.de). Die Zielgruppe sind weitestgehend Männer mit entsprechendem Einkommen.
Aufgabenstellung
Die Karte soll ein solches Maß haben, dass es in einen breiten Briefumschlag DIN Lang rein passt. Sie soll von beiden Seiten bunt bedruckt sein. Die Karte soll als Geschenkgutschein, z.B. zu Weihnachten verwendet werden. Das Design soll möglichst schörkellos sein und die Natur und das Tier in den Vordergrund stellen. Fleisch, z.B. Grillfleisch, soll nicht zu sehen sein.

```html
<!DOCTYPE html>
<html lang="de">
<head>
<meta charset="utf-8">
<title>Weidenkorn Geschenkgutschein</title>
<link href="https://fonts.googleapis.com/css2?family=Playfair+Display:wght@400&family=Libre+Baskerville:wght@400;700&display=swap" rel="stylesheet">
<style>
  :root {
    --page: #eeeeee;
    --card: #ffffff;
    --gold: #c9a470;
    --band: #58575a;
    --ink: #1c1a18;
    --label: #8a8580;
    --footer: #cba878;
  }
  * { margin: 0; padding: 0; box-sizing: border-box; }
  html, body { width: 1142px; height: 1200px; overflow: hidden; background: var(--page); }
  .canvas { position: relative; width: 1142px; height: 1200px; }

  .card {
    position: absolute; left: 79px; width: 985px; height: 469px;
    background: var(--card);
    box-shadow: 0 2px 8px rgba(0,0,0,0.14);
    overflow: hidden;
  }

  /* Vorderseite */
  .card--front { top: 78px; }
  .front__photo {
    position: absolute; left: 17px; top: 17px; width: 951px; height: 367px;
    background: linear-gradient(180deg,
      #9cc4e3 0%, #e6ebf0 14%, #c9d1da 30%, #7e8f9a 48%,
      #6a7c86 60%, #c99a3e 66%, #d8ab4c 80%, #c2913a 100%);
  }
  .front__band {
    position: absolute; left: 17px; top: 384px; width: 951px; height: 68px;
    background: var(--band);
    display: flex; align-items: center; justify-content: center; gap: 18px;
  }
  .front__title {
    font-family: "Playfair Display", serif; font-weight: 400;
    font-size: 38px; letter-spacing: 3px; color: var(--gold);
    line-height: 1;
  }
  .front__rule { width: 150px; height: 8px; display: block; }
  .brand {
    position: absolute; left: 416px; top: 17px; width: 168px; height: 116px;
    background: var(--card);
    display: flex; flex-direction: column; align-items: center; justify-content: flex-end;
    padding-bottom: 14px; gap: 18px;
  }
  .brand__mark { width: 34px; height: 34px; background: var(--ink); }
  .brand__name {
    font-family: "Libre Baskerville", serif; font-weight: 700;
    font-size: 18px; color: var(--ink); letter-spacing: 0.2px;
  }

  /* Rückseite */
  .card--back { top: 649px; }
  .back__photo {
    position: absolute; inset: 0 0 27px 0;
    background: linear-gradient(180deg,
      #c7d9e8 0%, #eef2f6 20%, #e4e9ee 35%, #f2f4f6 55%,
      #f7f7f8 75%, #ddd5cc 88%, #f5f5f6 100%);
  }
  .back__title {
    position: absolute; left: 0; right: 0; top: 62px; text-align: center;
    font-family: "Playfair Display", serif; font-weight: 400;
    font-size: 54px; letter-spacing: 4px; color: var(--gold); line-height: 1;
  }
  .field {
    position: absolute; height: 44px; background: var(--card);
    padding: 9px 0 0 11px;
    font-family: "Libre Baskerville", serif; font-size: 8.5px;
    letter-spacing: 0.6px; color: var(--label); text-transform: uppercase;
  }
  .field--value { left: 294px; top: 179px; width: 387px; }
  .field--recipient { left: 294px; top: 238px; width: 387px; }
  .field--number { left: 294px; top: 300px; width: 188px; padding-left: 6px; }
  .field--date { left: 490px; top: 300px; width: 189px; }

  .back__footer {
    position: absolute; left: 0; bottom: 0; width: 985px; height: 27px;
    background: var(--footer);
    display: flex; align-items: center; justify-content: space-between;
    padding: 0 86px 0 88px;
    font-family: "Libre Baskerville", serif; font-size: 8.5px;
    letter-spacing: 0.6px; color: #ffffff; text-transform: uppercase;
  }
</style>
</head>
<body>
<div class="canvas">

  <section class="card card--front">
    <div class="front__photo" role="img" aria-label="Bison steht in goldenem Präriegras vor verschneiten Bergen und Nadelwald"></div>
    <div class="brand">
      <span class="brand__mark"></span>
      <span class="brand__name">WEIDENKORN</span>
    </div>
    <div class="front__band">
      <svg class="front__rule" viewBox="0 0 150 8" aria-hidden="true">
        <line x1="0" y1="4" x2="150" y2="4" stroke="#c9a470" stroke-width="1.2"/>
      </svg>
      <h1 class="front__title">GESCHENKGUTSCHEIN</h1>
      <svg class="front__rule" viewBox="0 0 150 8" aria-hidden="true">
        <line x1="0" y1="4" x2="150" y2="4" stroke="#c9a470" stroke-width="1.2"/>
      </svg>
    </div>
  </section>

  <section class="card card--back">
    <div class="back__photo" role="img" aria-label="Blasse, verschneite Winterlandschaft mit Hügeln und einer grasenden Bisonherde"></div>
    <h2 class="back__title">GUTSCHEIN</h2>
    <div class="field field--value">Im Wert von</div>
    <div class="field field--recipient">Für</div>
    <div class="field field--number">Gutschein-Nr.</div>
    <div class="field field--date">Datum</div>
    <footer class="back__footer">
      <span>Weidenkorn UG</span>
      <span>Am Mühlenweg 12</span>
      <span>38700 Birkenfeld</span>
      <span>05321-4471820</span>
      <span>info@weidenkorn.de</span>
      <span>www.weidenkorn.de</span>
    </footer>
  </section>

</div>
</body>
</html>
```